Candle Rental Business seeks new website design

We need a new website design for a Candle hire business. The business rents out pillar candles for events such as weddings and corporate events. Our main target market is weddings. The business name is Hire a Lantern. The business name does not have a logo design.

We would like a website that is light in colours and creates a warm atmosphere. The design needs to be elegant and upmarket. There are different size candles that we hire out, ranging from 10cm diameter to 20cm diameter, flat, tall etc. All our candles are white in colour. Its just the size that differs.

We would also like to include a section for hiring out decor such as glassvases, candlebras, overlays and chairs sachets, chair covers. However, this is not the businesses main focus but an additional offering to customers.

Target Market(s)

Wedding venues and brides. Corporate events. School dances.

Industry/Entity Type

Hospitality

Logo Text

Hire a Lantern

Number of Pages Required

1 page

Font styles to use
Sans Serif
Script

Requirements
Must have
• Pictures of pillar candles. Plain white candles. The website must centre around candles.
Nice to have
• Different examples of candle centrepieces
Should not have
• Pictures must not be of brides. Pictures of surrounding is perferable.

```html
<!DOCTYPE html>
<html lang="en">
<head>
<meta charset="utf-8">
<title>Hire a Lantern — Candle Hire</title>
<link href="https://fonts.googleapis.com/css2?family=Patua+One&family=Lato:wght@400;700;900&family=Courgette&display=swap" rel="stylesheet">
<style>
:root{
  --pink:#f59ac8;
  --pink-deep:#e67fb3;
  --pink-text:#e8609f;
  --lilac-1:#c98ee9;
  --lilac-2:#b27fdb;
  --lilac-3:#a070cb;
  --purple:#9b5fcf;
  --grey-bg:#efefef;
  --text:#777;
  --heading:#8c8c8c;
  --footer:#333;
  --white:#fff;
}
*{box-sizing:border-box;margin:0;padding:0}
html,body{width:1200px;height:3186px;overflow:hidden}
body{font-family:"Lato",sans-serif;color:var(--text);background:#fff;position:relative}
.abs{position:absolute}
.slab{font-family:"Patua One",serif}

/* header */
.topbar{top:0;left:0;width:1200px;height:26px;background:var(--pink-deep);color:#fff;font-size:12px;font-weight:700}
.topbar span{position:absolute;top:6px}
.header{top:26px;left:0;width:1200px;height:76px;background:var(--pink)}
.brand{left:123px;top:16px;display:flex;align-items:center;gap:12px;color:#fff;font-family:"Patua One",serif;font-size:34px}
.brand i{display:block;width:44px;height:44px;border-radius:50%;background:#fff}
.nav{left:488px;top:29px;display:flex;gap:26px;font-size:13px;font-weight:900;color:#fff;letter-spacing:.3px}
.nav .active{border-bottom:3px solid #fff;padding-bottom:10px}

/* hero */
.hero{top:102px;left:0;width:1200px;height:433px;background:linear-gradient(90deg,#b98f6e 0%,#d8c6ad 30%,#ece6d9 55%,#cfdcb0 80%,#e9ead8 100%)}
.hero-arrow{top:205px;width:32px;height:32px;background:#333;display:flex;align-items:center;justify-content:center}
.hero-badge{left:446px;top:64px;width:306px;height:306px;border-radius:50%;background:rgba(255,255,255,.9);text-align:center;padding-top:80px}
.hero-badge p{font-family:"Patua One",serif;color:#777;font-size:22px;line-height:34px;letter-spacing:1px}
.hero-badge em{display:block;font-family:"Courgette",cursive;font-style:normal;color:var(--purple);font-size:36px;line-height:42px}

/* services */
.service{top:535px;width:400px;height:287px;color:#fff;text-align:center;padding-top:28px}
.service h3{font-family:"Patua One",serif;font-size:31px;font-weight:400;margin-top:12px}
.service p{font-size:13px;line-height:18px;margin:10px auto 0;width:300px}
.service .go{width:32px;height:32px;background:#fff;margin:14px auto 0;display:flex;align-items:center;justify-content:center}

/* section heading */
.sec-title{left:0;width:1200px;text-align:center;font-family:"Patua One",serif;font-size:32px;color:var(--heading)}
.sec-title b{font-weight:400;color:var(--pink-text)}
.sec-title::after{content:"";display:block;width:80px;height:2px;background:#aaa;margin:14px auto 0}

/* welcome */
.welcome-photo{left:119px;top:943px;width:254px;height:254px;border-radius:50%;background:radial-gradient(circle at 50% 60%,#f6ead4,#cdbba0 60%,#8f8068)}
.welcome-text{left:404px;top:948px;width:660px;font-size:13px;line-height:23px}
.welcome-text .lead{color:var(--pink-text);font-weight:700;font-size:14px;margin-bottom:14px}
.welcome-text p{margin-bottom:14px}
.welcome-text .more{color:var(--purple);font-weight:900;font-size:11px}

/* decor */
.decor{top:1281px;left:0;width:1200px;height:656px;background:var(--grey-bg)}
.decor-item{left:590px;width:500px;height:80px}
.decor-item .ic{position:absolute;left:0;top:0;width:76px;height:76px;border-radius:50%;background:#fff;border:4px solid #e3e3e3;display:flex;align-items:center;justify-content:center}
.decor-item h4{position:absolute;left:90px;top:0;font-family:"Patua One",serif;font-weight:400;font-size:19px;color:var(--pink-text)}
.decor-item p{position:absolute;left:90px;top:30px;width:400px;font-size:13px;line-height:22px}
.decor-item hr{position:absolute;left:90px;top:86px;width:320px;border:0;border-top:1px solid #d6d6d6}

/* promo */
.promo{top:1937px;left:0;width:1200px;height:480px;background:linear-gradient(90deg,#4b2b3b 0%,#7b4a78 35%,#8a4fa3 60%,#6b3a86 100%)}
.promo-candles{left:110px;top:80px;width:360px;height:360px;border-radius:40px;background:radial-gradient(ellipse at 50% 45%,#f5efe8,#c8b0b8 45%,rgba(120,70,110,0) 72%)}
.promo-text{left:529px;top:84px;width:620px;color:#fff;font-weight:700;font-size:21px;line-height:31px}
.promo-text h2{font-family:"Lato",sans-serif;font-weight:900;font-size:24px;letter-spacing:.5px}
.buy{left:529px;top:291px;width:110px;height:110px;border-radius:50%;background:var(--lilac-2);color:#fff;text-align:center;font-weight:900;font-size:16px;padding-top:38px}

/* testimonial */
.avatar{left:149px;top:2556px;width:118px;height:118px;border-radius:50%;border:4px solid #eee;background:radial-gradient(circle,#c9a690,#7a5a48)}
.client{left:291px;top:2596px}
.client h5{font-family:"Patua One",serif;font-weight:400;font-size:19px;color:var(--purple)}
.client span{font-size:13px}
.quote{left:480px;top:2568px;width:575px;font-size:13px;line-height:23px}
.quote q{quotes:"\201C" "\201D"}
.quote q::before,.quote q::after{color:var(--lilac-1);font-size:26px;font-family:Georgia,serif}
.dots{top:2705px;left:548px;display:flex;gap:10px}
.dots i{width:13px;height:13px;border:1px solid #999;border-radius:50%}
.dots i.on{background:#999}

/* partners */
.partners{top:2755px;left:0;width:1200px;height:127px;background:var(--grey-bg);display:flex;justify-content:center;align-items:center;gap:48px}
.partners span{width:130px;height:44px;border-radius:22px;background:#dcdcdc}

/* footer */
.scallop{top:2882px;left:0;width:1200px;height:10px;background:repeating-radial-gradient(circle at 8px 0,var(--pink) 0 7px,transparent 8px) ,linear-gradient(var(--lilac-2),var(--lilac-2));background-size:16px 10px,100% 3px;background-repeat:repeat-x,no-repeat}
.footer{top:2892px;left:0;width:1200px;height:294px;background:var(--footer);color:#ccc;font-size:12px}
.fcol{position:absolute;top:40px}
.fcol h6{color:#fff;font-size:13px;font-weight:900;margin-bottom:14px}
.fcol li{list-style:none;line-height:23px}
.fcol li::before{content:"› ";color:#fff}
.fcol input{display:block;width:172px;height:30px;border:0;margin:12px 0;padding-left:8px;font-size:12px}
.fcol .btn{display:inline-block;background:var(--lilac-2);color:#fff;padding:5px 12px;font-size:12px;font-weight:700}
.news{margin-bottom:14px}
.news b{color:#fff}
.fbrand{color:#fff;font-family:"Patua One",serif;font-size:21px;display:flex;align-items:center;gap:8px;margin-bottom:8px}
.fbrand i{width:28px;height:28px;border-radius:50%;background:#fff}
.copy{left:161px;top:258px}
.social{left:936px;top:252px;display:flex;gap:6px}
.social i{width:20px;height:20px;background:#555}
.social i:first-child{background:var(--lilac-2)}
</style>
</head>
<body>

<div class="abs topbar">
  <span style="left:828px">☎ 555-014-2290</span>
  <span style="left:940px">✉ info@hirealantern.com</span>
</div>
<header class="abs header">
  <div class="abs brand"><i></i>Hire A Lantern</div>
  <nav class="abs nav">
    <span class="active">HOME</span><span>ABOUT US</span><span>OUR PRODUCTS</span><span>HIRE CANDLES</span><span>DÉCOR HIRE</span><span>CONTACT US</span>
  </nav>
</header>

<section class="abs hero" role="img" aria-label="Table centrepiece of white pillar candles in glass with cream roses on a set wedding table">
  <div class="abs hero-arrow" style="left:10px"><svg width="12" height="14"><path d="M9 1 3 7l6 6" stroke="#fff" stroke-width="2.5" fill="none"/></svg></div>
  <div class="abs hero-arrow" style="left:1158px"><svg width="12" height="14"><path d="M3 1l6 6-6 6" stroke="#fff" stroke-width="2.5" fill="none"/></svg></div>
  <div class="abs hero-badge">
    <p>WE DESIGN,<br>MANUFACTURE<br>&amp; PERSONALISE</p>
    <em>Decorative<br>Candles</em>
  </div>
</section>

<section class="abs service" style="left:0;background:var(--lilac-1)">
  <svg width="44" height="66" viewBox="0 0 44 66"><path d="M22 2c6 8 8 14 0 22-8-8-6-14 0-22z" fill="#fff"/><rect x="8" y="28" width="28" height="36" rx="3" fill="#fff"/></svg>
  <h3>Hire Candles</h3>
  <p>Lorem ipsum dolor sit amet, consectetuer adipiscing elit, sed diam nonummy nibh euismod tincidunt</p>
  <div class="go"><svg width="10" height="14"><path d="M2 1l6 6-6 6" stroke="#a070cb" stroke-width="2.5" fill="none"/></svg></div>
</section>
<section class="abs service" style="left:400px;background:var(--lilac-2)">
  <svg width="96" height="66" viewBox="0 0 96 66"><path d="M30 10c5 7 6 12 0 18-6-6-5-11 0-18zM66 2c5 7 6 12 0 18-6-6-5-11 0-18z" fill="#fff"/><rect x="12" y="36" width="36" height="26" rx="3" fill="#fff"/><rect x="48" y="30" width="36" height="32" rx="3" fill="#fff"/></svg>
  <h3>Personalised Candles</h3>
  <p>Lorem ipsum dolor sit amet, consectetuer adipiscing elit, sed diam nonummy nibh euismod tincidunt</p>
  <div class="go"><svg width="10" height="14"><path d="M2 1l6 6-6 6" stroke="#a070cb" stroke-width="2.5" fill="none"/></svg></div>
</section>
<section class="abs service" style="left:800px;background:var(--lilac-3)">
  <svg width="70" height="66" viewBox="0 0 70 66"><path d="M35 2c4 5 4 9 0 13-4-4-4-8 0-13zM14 14c4 5 4 9 0 13-4-4-4-8 0-13zM56 14c4 5 4 9 0 13-4-4-4-8 0-13z" fill="#fff"/><rect x="29" y="18" width="12" height="30" fill="#fff"/><rect x="8" y="30" width="12" height="18" fill="#fff"/><rect x="50" y="30" width="12" height="18" fill="#fff"/><path d="M6 48h58l-8 10H14z" fill="#fff"/><rect x="30" y="58" width="10" height="6" fill="#fff"/></svg>
  <h3>Décor Hire</h3>
  <p>Lorem ipsum dolor sit amet, consectetuer adipiscing elit, sed diam nonummy nibh euismod tincidunt</p>
  <div class="go"><svg width="10" height="14"><path d="M2 1l6 6-6 6" stroke="#a070cb" stroke-width="2.5" fill="none"/></svg></div>
</section>

<h2 class="abs sec-title" style="top:866px">Welcome To <b>Hire A Lantern</b></h2>
<div class="abs welcome-photo" role="img" aria-label="White pillar candles beside a vase of white flowers"></div>
<div class="abs welcome-text">
  <p class="lead">Candles Create A Warm Atmosphere And Special Touch To All Occasions.It Is Much Cheaper Renting Than Buying Candles For Your Event.</p>
  <p>We DESIGN, MANUFACTURE, and PERSONALISE all of our CANDLES in our most distinctive handcrafted manner! Whether you are looking for candles for a wedding, birthday, anniversary, engagement, graduation, bridal or baby showers, baby christening, retirement, or any special occasion candles you can order it from us.</p>
  <p>We are a family owned and operated company and began making decorative candles for all occasions. All of our candles are individually hand made in our candle studio, situated in Millbrook, outside Harbourton. Our wax is local and of a very high quality, and dripless! Our wax is also made with a high melting point, which means it will not melt or bend in hot temperatures.</p>
  <span class="more">READ MORE</span>
</div>

<section class="abs decor">
  <h2 class="abs sec-title" style="top:46px">Our <b>Hiring Out Decor</b></h2>
  <svg class="abs" style="left:190px;top:220px" width="400" height="340" viewBox="0 0 400 340">
    <path d="M248 30 A152 152 0 0 1 248 310" stroke="#a070cb" stroke-width="6" fill="none"/>
    <g stroke="#ccc" stroke-width="2" fill="none">
      <path d="M296 110 L330 60 H400"/><path d="M312 170 H400"/><path d="M296 230 L330 240 H400"/><path d="M248 310 L290 330 H400"/>
    </g>
    <g fill="#e07aa9"><circle cx="296" cy="110" r="7"/><circle cx="312" cy="170" r="7"/><circle cx="296" cy="230" r="7"/></g>
    <path d="M146 170 L146 34 A136 136 0 0 0 10 170Z" fill="#e58fba"/>
    <path d="M146 170 L282 170 A136 136 0 0 0 146 34Z" fill="#d873a8"/>
    <path d="M146 170 L146 306 A136 136 0 0 0 282 170Z" fill="#f06fae"/>
    <path d="M146 170 L10 170 A136 136 0 0 0 146 306Z" fill="#f27fb8"/>
    <circle cx="146" cy="170" r="72" fill="#f4f4f4"/>
    <circle cx="146" cy="170" r="52" fill="#9b5fcf"/>
    <path d="M146 145c4 5 4 9 0 12-4-3-4-7 0-12z M134 160h24v26h-24z" fill="#fff"/>
    <g fill="#fff" font-family="Lato,sans-serif" font-size="14">
      <text transform="translate(60 110) rotate(-42)">Glass Vases</text>
      <text transform="translate(178 72) rotate(42)">Candle Bars</text>
      <text transform="translate(52 218) rotate(48)">Chair Covers</text>
      <text transform="translate(176 272) rotate(-48)">Chair Sachets</text>
    </g>
  </svg>
  <div class="abs decor-item" style="top:140px"><div class="ic"><svg width="26" height="36"><path d="M8 2h10l-2 8 6 24H4l6-24z" fill="#777"/></svg></div><h4>Glass Vases</h4><p>Lorem ipsum dolor sit amet, consectetuer adipiscing elit, sed diam nonummy nibh euismod tincidunt ut laoreet</p><hr></div>
  <div class="abs decor-item" style="top:268px"><div class="ic"><svg width="36" height="36"><path d="M18 4v26M6 8v10q0 8 12 8t12-8V8M10 34h16" stroke="#777" stroke-width="3" fill="none"/></svg></div><h4>Candle Bars</h4><p>Lorem ipsum dolor sit amet, consectetuer adipiscing elit, sed diam nonummy nibh euismod tincidunt ut laoreet</p><hr></div>
  <div class="abs decor-item" style="top:399px"><div class="ic"><svg width="30" height="36"><path d="M6 34V12a9 9 0 0 1 18 0v22M6 22h18" stroke="#777" stroke-width="3" fill="none"/></svg></div><h4>Overlays &amp; Chair Sachets</h4><p>Lorem ipsum dolor sit amet, consectetuer adipiscing elit, sed diam nonummy nibh euismod tincidunt ut laoreet</p><hr></div>
  <div class="abs decor-item" style="top:527px"><div class="ic"><svg width="38" height="30"><path d="M4 12h30v12H4zM8 12V4h22v8M6 24v4M32 24v4" stroke="#777" stroke-width="3" fill="none"/></svg></div><h4>Chair Covers</h4><p>Lorem ipsum dolor sit amet, consectetuer adipiscing elit, sed diam nonummy nibh euismod tincidunt ut laoreet</p><hr></div>
</section>

<section class="abs promo" role="img" aria-label="Two white pillar candles with festive ornaments in warm purple light">
  <div class="abs promo-candles"></div>
  <div class="abs promo-text">
    <h2>We DESIGN, MANUFACTURE &amp; PERSONALISE</h2>
    <p>All Of Our CANDLES In Our Most Distinctive<br>Handcrafted Manner!</p>
    <p style="margin-top:18px">Different Size Candles Ranging From<br>10cm Diameter To 20cm Diameter, Flat, Tall Etc</p>
  </div>
  <div class="abs buy">BUY NOW<br>»</div>
</section>

<h2 class="abs sec-title" style="top:2469px">What Our <b>Clients Say</b></h2>
<div class="abs avatar" role="img" aria-label="Client portrait"></div>
<div class="abs client"><h5>Dana Whitfield</h5><span>Home Maker</span></div>
<div class="abs quote"><q>Lorem ipsum dolor sit amet, consectetuer adipiscing elit, sed diam nonummy nibh euismod tincidunt ut laoreet dolore magna aliquam erat volutpat. Ut wisi enim ad minim veniam, quis nostrud exerci tation ullamcorper suscipit lobortis nisl ut aliquip ex ea commodo consequat.</q></div>
<div class="abs dots"><i></i><i class="on"></i><i></i><i></i></div>

<section class="abs partners"><span></span><span></span><span></span><span></span><span></span><span></span></section>

<div class="abs scallop"></div>
<footer class="abs footer">
  <div class="fcol" style="left:161px"><h6>QUICK LINK</h6><ul><li>Home</li><li>About Us</li><li>Our Products</li><li>Hire Candles</li><li>Décor Hire</li><li>Contact Us</li></ul></div>
  <div class="fcol" style="left:325px;width:200px"><h6>NEWSLETTER SIGN UP</h6><p>Lorem ipsum dolor sit amet, cons ectetuer adipiscing elit</p><input placeholder="Email Address"><span class="btn">SUBSCRIBE</span></div>
  <div class="fcol" style="left:595px;width:200px"><h6>LATEST NEWS</h6><p class="news"><b>▣ Lorem ipsum dolor sit amet</b><br>Lorem ipsum dolor sit amet, cons ectetuer adipiscing elit</p><p class="news"><b>▣ Lorem ipsum dolor sit amet</b><br>Lorem ipsum dolor sit amet, cons ectetuer adipiscing elit</p></div>
  <div class="fcol" style="left:856px;width:200px"><h6>GET IN TOUCH</h6><div class="fbrand"><i></i>Hire A Lantern</div><p>Lorem ipsum dolor sit amet, cons ectetuer adipiscing elit</p><p style="color:#fff;font-weight:700;margin-top:10px;line-height:24px">☎ 555-014-2290<br>☎ 555-014-2291</p></div>
  <p class="abs copy">Copyright © 2016 HIRE A LANTERN | All Rights Reserved.</p>
  <div class="abs social"><i></i><i></i><i></i><i></i></div>
</footer>

</body>
</html>
```